Logo & Visitenkarte für Logopädische Praxis
Zielgruppe
In meiner logopädischen Praxis geht es um Sprach-, Sprech- und Stimmtherapie. Meine Zielgruppe sind Erwachsene jeglichen Alters und Geschlechts.
Aufgabenstellung
Ich habe noch keine konkreten Vorstellungen.

```html
<!DOCTYPE html>
<html lang="de">
<head>
<meta charset="utf-8">
<title>Fridolin Kuberz – Logopädische Praxis – Visitenkarten</title>
<link rel="stylesheet" href="https://fonts.googleapis.com/css2?family=Exo+2:wght@500;600;700&family=Montserrat:wght@500;600;700&display=swap">
<style>
  :root {
    --teal: #23809a;
    --green: #5e9a20;
    --card-light: #f1f1f1;
    --backdrop: #e4e2e0;
    --ink: #1b1b1b;
    --white: #ffffff;
  }
  * { margin: 0; padding: 0; box-sizing: border-box; }
  html, body { width: 1200px; height: 968px; overflow: hidden; }
  body { background: var(--backdrop); position: relative; font-family: "Exo 2", sans-serif; }

  .card {
    position: absolute; left: 390px; width: 422px; height: 272px;
    box-shadow: 0 6px 14px rgba(0,0,0,.18);
    overflow: hidden;
  }
  .card--front { top: 27px; background: var(--teal); }
  .card--back-a { top: 342px; background: var(--card-light); }
  .card--back-b { top: 653px; background: var(--card-light); }

  .brand-dot { position: absolute; border-radius: 50%; }
  .card--front .brand-dot { left: 155px; top: 66px; width: 94px; height: 94px; background: var(--white); }
  .card--back-a .brand-dot, .card--back-b .brand-dot { left: 260px; top: 57px; width: 82px; height: 82px; background: var(--teal); }

  .brand-name {
    position: absolute; left: 0; width: 100%; text-align: center;
    font-family: "Exo 2", sans-serif; font-weight: 700; letter-spacing: .01em; line-height: 1;
  }
  .card--front .brand-name { top: 171px; font-size: 22px; color: var(--white); }
  .brand-tagline {
    position: absolute; left: 0; width: 100%; text-align: center;
    font-family: "Montserrat", sans-serif; font-weight: 700; line-height: 1;
  }
  .card--front .brand-tagline { top: 198px; font-size: 11px; letter-spacing: .42em; color: var(--white); padding-left: .42em; }

  .back-brand { position: absolute; left: 206px; width: 210px; }
  .back-brand .brand-name { top: 148px; font-size: 18px; color: var(--teal); }
  .back-brand .brand-tagline { top: 171px; font-size: 9.5px; letter-spacing: .38em; color: var(--green); padding-left: .38em; }

  .holder-name {
    position: absolute; left: 13px; top: 20px;
    font-family: "Exo 2", sans-serif; font-weight: 500; font-size: 23px;
    color: var(--teal); letter-spacing: .01em; line-height: 1;
  }
  .holder-rule { position: absolute; left: 10px; top: 46px; width: 232px; height: 2px; background: var(--teal); }

  .taper { position: absolute; left: 13px; width: 120px; height: 4px; }
  .taper--top { top: 61px; }
  .taper--bottom { top: 124px; }

  .address {
    position: absolute; left: 16px; top: 72px;
    font-family: "Exo 2", sans-serif; font-weight: 600; font-size: 9.6px; line-height: 12px;
    color: var(--teal);
  }

  .contact { position: absolute; left: 12px; display: flex; align-items: center; gap: 6px; }
  .contact--phone { top: 144px; }
  .contact--mail { top: 178px; }
  .contact-icon { width: 26px; height: 26px; }
  .contact-text { font-family: "Montserrat", sans-serif; color: var(--ink); }
  .contact--phone .contact-text { font-size: 12px; font-weight: 500; }
  .contact--mail .contact-text { font-size: 6.5px; font-weight: 700; text-transform: uppercase; }

  .web-band {
    position: absolute; left: 0; top: 224px; width: 240px; height: 25px;
    background: var(--green); color: var(--white);
    font-family: "Montserrat", sans-serif; font-weight: 500; font-size: 12px;
    line-height: 25px; padding-left: 13px;
  }
  .web-line { position: absolute; left: 240px; top: 234px; right: 0; height: 5px; background: var(--green); }
</style>
</head>
<body>

<section class="card card--front">
  <span class="brand-dot"></span>
  <p class="brand-name">FRIDOLIN KUBERZ</p>
  <p class="brand-tagline">LOGOPÄDISCHE PRAXIS</p>
</section>

<section class="card card--back-a">
  <h2 class="holder-name">FRIDOLINKUBERZ</h2>
  <span class="holder-rule"></span>
  <svg class="taper taper--top" viewBox="0 0 120 4" preserveAspectRatio="none"><polygon points="0,0 120,1.5 120,2.5 0,4" fill="#5e9a20"/></svg>
  <p class="address">KIEFERORTHOPÄDISCHE FACHZAHNARZTPRAXIS<br>JONAS WELTERBACH,<br>LINDENHOFER STRAẞE 7<br>27341 WIESENBRÜCK</p>
  <svg class="taper taper--bottom" viewBox="0 0 120 4" preserveAspectRatio="none"><polygon points="0,0 120,1.5 120,2.5 0,4" fill="#5e9a20"/></svg>
  <div class="contact contact--phone">
    <svg class="contact-icon" viewBox="0 0 26 26" aria-hidden="true"><circle cx="13" cy="13" r="13" fill="#23809a"/><path d="M9 7.5c.8-.5 1.6-.3 2 .5l1 2c.3.6.1 1.2-.4 1.6l-.8.6c.6 1.5 1.7 2.7 3.2 3.4l.6-.8c.4-.5 1-.7 1.6-.4l2 1c.8.4 1 1.2.5 2l-.7 1c-.6.8-1.7 1.1-2.7.7-3.4-1.3-6-3.9-7.2-7.3-.4-1 0-2.1.8-2.7z" fill="#fff"/></svg>
    <span class="contact-text">01234-550917</span>
  </div>
  <div class="contact contact--mail">
    <svg class="contact-icon" viewBox="0 0 26 26" aria-hidden="true"><circle cx="13" cy="13" r="13" fill="#23809a"/><rect x="7" y="9" width="12" height="8.5" fill="#fff"/><polyline points="7,9 13,14 19,9" fill="none" stroke="#23809a" stroke-width="1.2"/></svg>
    <span class="contact-text">info@praxis-kuberz.de</span>
  </div>
  <div class="web-band">www.praxis-kuberz.de</div>
  <span class="web-line"></span>
  <div class="back-brand">
    <p class="brand-name">FRIDOLIN KUBERZ</p>
    <p class="brand-tagline">LOGOPÄDISCHE PRAXIS</p>
  </div>
  <span class="brand-dot"></span>
</section>

<section class="card card--back-b">
  <h2 class="holder-name">FRIDOLINKUBERZ</h2>
  <span class="holder-rule"></span>
  <svg class="taper taper--top" viewBox="0 0 120 4" preserveAspectRatio="none"><polygon points="0,0 120,1.5 120,2.5 0,4" fill="#5e9a20"/></svg>
  <p class="address">KIEFERORTHOPÄDISCHE FACHZAHNARZTPRAXIS<br>JONAS WELTERBACH,<br>LINDENHOFER STRAẞE 7<br>27341 WIESENBRÜCK</p>
  <svg class="taper taper--bottom" viewBox="0 0 120 4" preserveAspectRatio="none"><polygon points="0,0 120,1.5 120,2.5 0,4" fill="#5e9a20"/></svg>
  <div class="contact contact--phone">
    <svg class="contact-icon" viewBox="0 0 26 26" aria-hidden="true"><circle cx="13" cy="13" r="13" fill="#23809a"/><path d="M9 7.5c.8-.5 1.6-.3 2 .5l1 2c.3.6.1 1.2-.4 1.6l-.8.6c.6 1.5 1.7 2.7 3.2 3.4l.6-.8c.4-.5 1-.7 1.6-.4l2 1c.8.4 1 1.2.5 2l-.7 1c-.6.8-1.7 1.1-2.7.7-3.4-1.3-6-3.9-7.2-7.3-.4-1 0-2.1.8-2.7z" fill="#fff"/></svg>
    <span class="contact-text">01234-550917</span>
  </div>
  <div class="contact contact--mail">
    <svg class="contact-icon" viewBox="0 0 26 26" aria-hidden="true"><circle cx="13" cy="13" r="13" fill="#23809a"/><rect x="7" y="9" width="12" height="8.5" fill="#fff"/><polyline points="7,9 13,14 19,9" fill="none" stroke="#23809a" stroke-width="1.2"/></svg>
    <span class="contact-text">info@praxis-kuberz.de</span>
  </div>
  <div class="web-band">www.praxis-kuberz.de</div>
  <span class="web-line"></span>
  <div class="back-brand">
    <p class="brand-name">FRIDOLIN KUBERZ</p>
    <p class="brand-tagline">LOGOPÄDISCHE PRAXIS</p>
  </div>
  <span class="brand-dot"></span>
</section>

</body>
</html>
```